New Creative Busines Card

Hi Lead Designer,

How are you going?

I was hoping you can help me design the perfect business card for my new business. I have listed below some background information about the business and the concept to help with your design. I'm open to any form of creative ideas, but would like to have two types of colour schemes one dark color and one light.

I would like to have a dark set of design and a light (One design with one in black or dark background and one with light background to compare the contrast since the business card will be double sided one) I imagine this will be pretty easy to change the background of the design. Would prefer one side to have all the details and the other will just have a amazing logo (K7) to give it the finishing touch.

Feel free to email me if you have any questions.

Business Structure and design concepts:

Name of the business: K7 Advisory
Business: Dating agency and event management (Date night etc)
Concept: The main focus will be the K7 ( As some sort of a heart shape like logo) be creative
Details to include in the card will be general details like Name, Title: , Email, mobile, website (Contact details will be given later).

The rest of the idea is up to you, feel free to go crazy with your creative ideas.

Thank you for your help in advance, may the best candidate win~!

Target Market(s)

Target market will be Professional, Elegant, young and ambitious people.

Industry/Entity Type

Business

Requirements
Must have
• Focus on the K7 (as some sort of a heart shape logo). Since this is a double sides design would prefer on one side to focus on the just the K7 logo and the other side with a smaller version of the logo (with it or without) and all the details such as Name, Title, Mobile, Email, Website. Please have the design in landscape format.Not fuss with the Font as long as it is easy to read.
Nice to have
• Different Contrast in colours (keep it simple) one side dark colour scheme and one side light. Prefer to have 3-4 colours (not overwhelm with too many colours) to keep it simple and elegant.
Should not have
• Too colours, main focus is should be the K7 logo not the colours

```html
<!DOCTYPE html>
<html lang="en">
<head>
<meta charset="utf-8">
<title>K7 Advisory – Business Card</title>
<link href="https://fonts.googleapis.com/css2?family=Exo+2:wght@500;600&family=Open+Sans:wght@400&display=swap" rel="stylesheet">
<style>
  :root {
    --pink: #e2007a;
    --cyan: #2aa9dd;
    --blue: #1172b8;
    --white: #ffffff;
    --divider: #c9c9c9;
    --stage: #444446;
    --brand-font: "Exo 2", sans-serif;
    --body-font: "Open Sans", sans-serif;
  }
  * { margin: 0; padding: 0; box-sizing: border-box; }
  html, body { width: 1198px; height: 1200px; overflow: hidden; }
  body { position: relative; background: var(--stage); font-family: var(--body-font); }

  .stage { position: absolute; left: 0; top: 0; width: 1198px; height: 900px; background: var(--stage); }

  .card {
    position: absolute;
    top: 298px;
    width: 530px;
    height: 303px;
    overflow: hidden;
    box-shadow: 0 6px 18px rgba(0,0,0,.35);
  }

  /* Front: details side */
  .card--front { left: 40px; background: var(--white); }
  .card--front .edge { position: absolute; bottom: 0; height: 10px; }
  .card--front .edge--pink { left: 0; width: 46%; background: var(--pink); }
  .card--front .edge--cyan { right: 0; width: 54%; background: var(--cyan); }
  .card--front .divider {
    position: absolute; left: 46%; top: 52px; width: 1px; height: 170px; background: var(--divider);
  }
  .card--front .brand {
    position: absolute; left: 0; width: 46%; top: 0; height: 293px;
    display: flex; flex-direction: column; align-items: center; justify-content: center; gap: 14px;
  }
  .brand-mark { width: 22px; height: 22px; border-radius: 50%; background: var(--pink); }
  .brand-name {
    font-family: var(--brand-font); font-weight: 600; letter-spacing: 1px;
    text-transform: uppercase; white-space: nowrap;
  }
  .card--front .brand-name { color: var(--cyan); font-size: 28px; }

  .contact { position: absolute; left: 52%; top: 50px; right: 20px; }
  .contact .person { font-family: var(--body-font); color: var(--cyan); font-size: 25px; line-height: 1.05; }
  .contact .role { color: var(--pink); font-size: 15px; margin-bottom: 14px; }
  .contact ul { list-style: none; }
  .contact li {
    display: flex; align-items: flex-start; gap: 10px;
    color: var(--cyan); font-size: 15px; line-height: 1.25; margin-bottom: 5px;
  }
  .contact svg { flex: none; width: 16px; height: 16px; margin-top: 1px; fill: none; stroke: var(--pink); stroke-width: 1.6; }
  .contact svg .solid { fill: var(--pink); stroke: none; }

  /* Back: brand side */
  .card--back { left: 628px; background: var(--pink); display: flex; align-items: center; justify-content: center; }
  .card--back .brand-name { color: var(--white); font-size: 46px; }

  /* Logo swatches */
  .swatch {
    position: absolute; top: 900px; height: 300px; width: 599px;
    display: flex; align-items: center; justify-content: center; gap: 16px;
  }
  .swatch .brand-name { font-size: 48px; }
  .swatch--light { left: 0; background: var(--white); }
  .swatch--light .brand-name { color: var(--cyan); }
  .swatch--dark { left: 599px; background: var(--blue); }
  .swatch--dark .brand-name { color: var(--white); }
</style>
</head>
<body>
  <section class="stage">
    <article class="card card--front">
      <div class="brand">
        <span class="brand-name">K7 Advisory</span>
      </div>
      <div class="divider"></div>
      <div class="contact">
        <p class="person">Name Surname</p>
        <p class="role">Manager</p>
        <ul>
          <li>
            <svg viewBox="0 0 16 16"><rect x="4" y="1" width="8" height="14" rx="1.5"/><circle class="solid" cx="8" cy="12.5" r="1"/></svg>
            0 12 345 67 89
          </li>
          <li>
            <svg viewBox="0 0 16 16"><path class="solid" d="M3 1.5l3 .5 1 3.5-2 1.5c1 2 2.5 3.5 4.5 4.5l1.5-2 3.5 1 .5 3c-1 1-2 1.5-3 1.5C6.5 15 1 9.5 1 4.5 1 3.5 1.8 2.3 3 1.5z"/></svg>
            0 12 345 67 89
          </li>
          <li>
            <svg viewBox="0 0 16 16"><circle cx="8" cy="8" r="6.5"/><ellipse cx="8" cy="8" rx="3" ry="6.5"/><path d="M1.5 8h13M2.5 4.5h11M2.5 11.5h11"/></svg>
            www.yoursite.com
          </li>
          <li>
            <svg viewBox="0 0 16 16"><rect x="1" y="3" width="14" height="10"/><path d="M1 3l7 6 7-6"/></svg>
            info@yoursite.com
          </li>
          <li>
            <svg viewBox="0 0 16 16"><path class="solid" d="M8 1a4.5 4.5 0 0 0-4.5 4.5C3.5 9 8 15 8 15s4.5-6 4.5-9.5A4.5 4.5 0 0 0 8 1zm0 6.3a1.8 1.8 0 1 1 0-3.6 1.8 1.8 0 0 1 0 3.6z"/></svg>
            Address line here 12<br>second line
          </li>
        </ul>
      </div>
      <div class="edge edge--pink"></div>
      <div class="edge edge--cyan"></div>
    </article>

    <article class="card card--back">
      <span class="brand-name">K7 Advisory</span>
    </article>
  </section>

  <section class="swatch swatch--light">
    <span class="brand-name">K7 Advisory</span>
  </section>
  <section class="swatch swatch--dark">
    <span class="brand-name">K7 Advisory</span>
  </section>
</body>
</html>
```